Enhance the web site presence of KRU Global Limited

Upgrade the current web site www.krucircuit-example.com to share with the audience our current plan and future developments of our company. I have created a worksheet which shows all the pages that I like to have. The home page in English, Japanese and Chinese is hyperlinked to the various pages. Under the product, we should allow the user to select "single sided PCB or double sided PCB". The translation of the contents of the pages with Japanese is not complete but the English and Chinese are complete. You can download the briefing and photos in the dropbox files below;

https://www.filebinvault-example.com/sh/x7k2mq9plw4rt8a/BBQZ_Hn462UdgnRtYmXzzYfLb?dl=0

Target Market(s)

Electronic companies

Industry/Entity Type

Electronic

Coding

Coded - Design and coding required

Number of Pages Required

5+ page

Font styles to use
Sans Serif

Colors
00a990
0353a1
33b8a4

Requirements
Must have
• Get a sense of confidence on our company's integrity and capability to deliver the highest quality PCBs with the most competitive prices and best services. A sense of elegance is essential as we DON'T treat profits as the number one goal. Our number goal is to do the RIGHT things right. Having a mixture of our company photos will be appropriate.

```html
<!DOCTYPE html>
<html lang="en">
<head>
<meta charset="utf-8">
<title>KRU Global Limited</title>
<link rel="stylesheet" href="https://fonts.googleapis.com/css2?family=Montserrat:wght@400;600;700&family=Open+Sans:wght@400;600;700&display=swap">
<style>
:root{
  --teal:#00a990;
  --teal-soft:#33b8a4;
  --blue:#0353a1;
  --ink:#222;
  --muted:#555;
  --paper:#ffffff;
  --mist:#efeff1;
  --night:#0b0b0b;
  --line:#2a2a2a;
}
*{box-sizing:border-box;margin:0;padding:0}
html,body{width:1200px;height:2484px;overflow:hidden}
body{position:relative;background:var(--paper);font-family:"Open Sans",Arial,sans-serif;color:var(--ink)}
.section{position:absolute;left:0;width:1200px}
.btn{display:inline-block;font-family:"Montserrat",Arial,sans-serif;font-weight:700;font-size:13px;letter-spacing:.5px;padding:12px 22px;text-transform:uppercase}
.btn-dark{background:#111;color:#fff}
.btn-light{background:#fff;color:#111}
.btn-teal{background:var(--teal);color:#fff}

/* hero */
.hero{top:0;height:560px;background:linear-gradient(160deg,#b9c1c4 0%,#8f9da0 40%,#6f8a84 70%,#97a6a3 100%)}
.hero-photo{position:absolute;inset:0}
.nav{position:absolute;top:0;left:0;width:1200px;height:70px;background:rgba(10,20,20,.72);display:flex;align-items:center;padding:0 60px}
.brand{display:flex;align-items:center;gap:10px;font-family:"Montserrat",Arial,sans-serif;font-weight:700;font-size:20px;color:#fff}
.brand-mark{width:22px;height:22px;background:var(--teal)}
.nav-links{margin-left:auto;display:flex;gap:28px;align-items:center;font-size:13px;color:#fff;font-weight:600}
.nav-links .signup{background:var(--teal);padding:8px 14px}
.hero-title{position:absolute;top:320px;width:100%;text-align:center;font-family:"Montserrat",Arial,sans-serif;font-weight:700;font-size:46px;color:#fff}
.hero-actions{position:absolute;top:422px;width:100%;display:flex;justify-content:center;gap:16px}

/* background */
.about{top:560px;height:280px;background:var(--mist);text-align:center}
.section-title{font-family:"Montserrat",Arial,sans-serif;font-weight:700;font-size:30px}
.about .section-title{margin-top:56px}
.section-text{width:1000px;margin:22px auto 26px;font-size:14px;line-height:1.6}

/* carousel */
.slider{top:928px;height:400px}
.slide-photo{position:absolute;top:0;height:362px}
.slide-left{left:0;width:262px;background:linear-gradient(180deg,#d7dce0,#aeb8bf)}
.slide-main{left:272px;width:680px;background:linear-gradient(170deg,#c9d2d6,#8c9ba2 60%,#6f7d85)}
.slide-right{left:962px;width:238px;background:linear-gradient(180deg,#dfe4e2,#a9b7b2)}
.slide-card{position:absolute;left:228px;top:28px;width:322px;height:236px;background:rgba(0,169,144,.92);color:#fff;padding:26px 26px}
.slide-card h3{font-family:"Montserrat",Arial,sans-serif;font-weight:700;font-size:23px;line-height:1.2;text-transform:uppercase}
.slide-card p{font-size:10px;line-height:1.5;margin:14px 0 18px;width:220px}
.slide-card .btn{border:1px solid #fff;padding:8px 14px;font-size:10px}
.slider-arrows{position:absolute;top:368px;left:938px;display:flex;gap:4px}

/* investment */
.invest{top:1344px;height:376px;background:var(--blue);color:#fff;text-align:center}
.invest .section-title{margin-top:62px}
.invest .section-text{font-size:13px;line-height:1.55;width:960px;margin:24px auto 30px}

/* partners */
.partners{top:1740px;height:380px;text-align:center}
.partners-intro{width:860px;margin:24px auto 0;font-size:13px;line-height:1.55}
.partner-row{position:absolute;top:80px;left:0;width:1200px;height:200px;background:var(--mist)}
.partner{position:absolute;top:0;height:200px;display:flex;align-items:center;justify-content:center;font-family:"Open Sans",Arial,sans-serif;font-weight:700;font-size:30px;color:#444}
.partner-featured{background:var(--teal);color:#fff;flex-direction:column;gap:14px;top:-10px;height:220px}
.partner-featured .chip{width:60px;height:60px;border:3px solid #fff;border-radius:50%}
.partners-more{position:absolute;top:334px;width:100%;font-size:12px;font-weight:700;letter-spacing:.5px}

/* footer */
.footer{top:2136px;height:348px;background:var(--night);color:#ccc;font-size:11px}
.footer h4{font-size:12px;font-weight:600;color:#eee;margin-bottom:14px}
.col{position:absolute;top:36px}
.form .field{width:100px;height:22px;background:#fff;margin-bottom:8px}
.form .pair{display:flex;gap:8px}
.form .message{width:208px;height:50px;background:#fff;margin-bottom:8px}
.form .send{width:70px;height:22px;background:#fff;color:#111;font-size:10px;font-weight:700;text-align:center;line-height:22px}
.info{display:flex;gap:8px;align-items:flex-start;margin-bottom:10px;line-height:1.5;width:250px}
.info svg{flex:none;margin-top:2px}
.footer-base{position:absolute;top:268px;left:0;width:1200px;border-top:1px solid var(--line);padding-top:22px}
.socials{position:absolute;left:160px;top:24px;display:flex;gap:14px}
.socials span{width:16px;height:16px;background:#ccc;display:block}
.legal{position:absolute;left:320px;top:20px;font-size:10px;line-height:1.6;color:#aaa}
.legal strong{color:#eee}
</style>
</head>
<body>

<header class="section hero">
  <div class="hero-photo" role="img" aria-label="Photo of the automated PCB production line inside the factory"></div>
  <nav class="nav">
    <div class="brand"><span class="brand-mark"></span>KRU Global</div>
    <div class="nav-links">
      <span>Home</span><span>Products</span><span>Our facilities</span><span>Customers</span><span>News</span><span>Contact Us</span><span>中文</span><span>EN</span><span>LOGIN</span><span class="signup">SIGN UP</span>
    </div>
  </nav>
  <h1 class="hero-title">Welcome to KRU Global Limited (KRU)</h1>
  <div class="hero-actions">
    <span class="btn btn-teal">Learn More</span>
    <span class="btn btn-light">Contact Us</span>
  </div>
</header>

<section class="section about">
  <h2 class="section-title">Company Background</h2>
  <p class="section-text">Established in 2007, KRU Global Limited (KRU) is a Hong Kong company specialising in single and double sided printed circuit boards. Its manufacturing facility is located in a self-owned facility in Lianhe, Qingshan of China which is 30 minutes from Hong Kong.</p>
  <span class="btn btn-dark">Learn More</span>
</section>

<section class="section slider">
  <div class="slide-photo slide-left" role="img" aria-label="Photo of inspection machines on the factory floor"></div>
  <div class="slide-photo slide-main" role="img" aria-label="Photo of circuit board processing equipment"></div>
  <div class="slide-photo slide-right" role="img" aria-label="Photo of finished boards stacked on racks"></div>
  <div class="slide-card">
    <h3>Single Layered Printed Circuit Boards</h3>
    <p>Reliable single sided boards built on automated lines, tested at every stage and shipped on schedule to our partners.</p>
    <span class="btn">Learn More</span>
  </div>
  <div class="slider-arrows">
    <svg width="12" height="12" viewBox="0 0 12 12"><rect width="12" height="12" fill="#333"/><path d="M7.5 3 4.5 6l3 3" stroke="#fff" stroke-width="1.5" fill="none"/></svg>
    <svg width="12" height="12" viewBox="0 0 12 12"><rect width="12" height="12" fill="#333"/><path d="M4.5 3l3 3-3 3" stroke="#fff" stroke-width="1.5" fill="none"/></svg>
  </div>
</section>

<section class="section invest">
  <h2 class="section-title">Our Investment And Upgrade</h2>
  <p class="section-text">Maintaining a highly automated factory is the only way to ensure consistent product and long term competitive efficiency. From 2015 to 2017, KRU invested over US$2.5 million in automating our production lines and upgrading our quality control, and we will invest a further US$1.5 million in 2018 to continue our improvement. Our aim is to remain one of the most efficient and highest quality single sided PCB manufacturers in Asia. By the end of 2018, 100% of our PCBs will be inspected by AOI before they are delivered to our customers.</p>
  <span class="btn btn-light">Learn More</span>
</section>

<section class="section partners">
  <p class="partners-intro">KRU is embracing a philosophy of being a partner with our customers. As a result, we are strategic PCB suppliers to the following world renowned companies:</p>
  <div class="partner-row">
    <div class="partner" style="left:60px;width:220px">Norvane</div>
    <div class="partner" style="left:340px;width:220px">Kestrel</div>
    <div class="partner partner-featured" style="left:700px;width:260px"><span>Duvela</span><span class="chip"></span></div>
    <div class="partner" style="left:980px;width:200px">Marlo</div>
  </div>
  <div class="partners-more">VIEW MORE PARTNERS</div>
</section>

<footer class="section footer">
  <div class="col form" style="left:160px">
    <h4>Contact Form</h4>
    <div class="pair"><div class="field"></div><div class="field"></div></div>
    <div class="pair"><div class="field"></div><div class="field"></div></div>
    <div class="message"></div>
    <div class="send">SEND</div>
  </div>
  <div class="col" style="left:600px">
    <h4>Factory Address</h4>
    <div class="info"><svg width="10" height="12" viewBox="0 0 10 12"><path d="M5 0a4 4 0 0 1 4 4c0 3-4 8-4 8S1 7 1 4a4 4 0 0 1 4-4z" fill="#ccc"/></svg><span>8 Qiaoxin Road, Lianhe Industrial Zone, Qingshan, China</span></div>
    <div class="info"><svg width="10" height="10" viewBox="0 0 10 10"><path d="M2 0l2 2-1 2 3 3 2-1 2 2-2 2C4 10 0 6 0 2z" fill="#ccc"/></svg><span>+86 769 0000 1234</span></div>
    <div class="info"><svg width="12" height="9" viewBox="0 0 12 9"><rect width="12" height="9" fill="#ccc"/><path d="M0 0l6 5 6-5" stroke="#0b0b0b" fill="none"/></svg><span>factory@krucircuit-example.com</span></div>
  </div>
  <div class="col" style="left:900px">
    <h4>Hong Kong Office</h4>
    <div class="info"><svg width="10" height="12" viewBox="0 0 10 12"><path d="M5 0a4 4 0 0 1 4 4c0 3-4 8-4 8S1 7 1 4a4 4 0 0 1 4-4z" fill="#ccc"/></svg><span>Unit 12, 9/F, Harbourline Centre, 88 Fenwick Lane, Kowloon</span></div>
    <div class="info"><svg width="10" height="10" viewBox="0 0 10 10"><path d="M2 0l2 2-1 2 3 3 2-1 2 2-2 2C4 10 0 6 0 2z" fill="#ccc"/></svg><span>+852 0000 5678</span></div>
    <div class="info"><svg width="12" height="9" viewBox="0 0 12 9"><rect width="12" height="9" fill="#ccc"/><path d="M0 0l6 5 6-5" stroke="#0b0b0b" fill="none"/></svg><span>hk@krucircuit-example.com</span></div>
  </div>
  <div class="footer-base">
    <div class="socials"><span></span><span></span><span></span></div>
    <div class="legal"><strong>Terms &amp; Conditions and Privacy Policy</strong><br>All content on this site belongs to KRU Global Limited and may not be reused without written consent.<br>© 2018 KRU Global Limited. All Rights Reserved.</div>
  </div>
</footer>

</body>
</html>
```